Automotive component supplier needs a business card design

We need a business card design for our company called Velmar Global Components Ltd based in the UK. We are a supplier of interior and exterior components to premium car manufacturers such as Corvane Hale, Durrant Fyfe, Maxtorn and Valdessimo. We would like to see a modern business card design that uses the colour blue.

Target Market(s)

Premium automotive car manufacturers.

Industry/Entity Type

Automotive

Contact Information for Business Card

Company Name : Velmar Global Components Limited
Address: 17 Tamsey Yard, Upper Drisk, Warwick, CV31 8RJ, United Kingdom
Web Address : www.velmarparts-example.co.uk

Font styles to use
Other font styles liked:
• Helvetica

Colors
3176b5
0255a3
85acd3
cfdeed
cee9f5
85cae6
34a6d7
0692cd
9bcb3c

Requirements
Must have
• Clear company logo and a mixture of blue colours.
Nice to have
• A high quality modern image.
Should not have
• Multiple colours.

```html
<!DOCTYPE html>
<html lang="en">
<head>
<meta charset="utf-8">
<title>Velmar Global Components – Business Card</title>
<link rel="stylesheet" href="https://fonts.googleapis.com/css2?family=Arimo:wght@400;700&display=swap">
<style>
  :root {
    --bg: #1c1d1f;
    --blue-deep: #0255a3;
    --blue-mid: #3176b5;
    --blue-bright: #0692cd;
    --blue-sky: #34a6d7;
    --green: #9bcb3c;
    --white: #ffffff;
    --rule: rgba(255,255,255,0.18);
  }
  * { margin: 0; padding: 0; box-sizing: border-box; }
  html, body { width: 1200px; height: 900px; overflow: hidden; background: var(--bg); }
  body { position: relative; font-family: "Arimo", Helvetica, Arial, sans-serif; }

  .card {
    position: absolute;
    width: 520px;
    height: 300px;
    border-radius: 22px;
    overflow: hidden;
    box-shadow: 0 18px 40px rgba(0,0,0,0.55);
  }

  /* Front */
  .card-front {
    left: 80px; top: 110px;
    background: radial-gradient(circle at 50% 55%, var(--blue-sky) 0%, var(--blue-bright) 70%, #0483c0 100%);
    display: flex; align-items: center; justify-content: center;
  }
  .brand {
    display: flex; align-items: center; gap: 12px;
    color: var(--white);
    font-weight: 700;
    font-size: 28px;
    letter-spacing: 0.5px;
    white-space: nowrap;
  }
  .brand-mark { width: 16px; height: 16px; background: var(--green); flex: none; }

  /* Back */
  .card-back { left: 600px; top: 500px; background: var(--white); }
  .card-back .shapes { position: absolute; inset: 0; }
  .card-back .brand {
    position: absolute; right: 48px; top: 48px;
    align-items: flex-start;
    color: var(--blue-bright);
    font-size: 21px;
    line-height: 1.15;
    gap: 9px;
  }
  .card-back .brand-mark { width: 12px; height: 12px; margin-top: 6px; }

  .contact { position: absolute; left: 34px; top: 46px; color: var(--white); width: 220px; }
  .contact-name { color: var(--green); font-weight: 700; font-size: 27px; line-height: 1; }
  .contact-role { font-weight: 700; font-size: 11px; margin-top: 6px; margin-bottom: 16px; letter-spacing: 0.3px; }
  .contact-group {
    font-size: 11.5px; line-height: 1.45;
    padding: 9px 0;
    border-top: 1px solid var(--rule);
  }
  .contact-group.small { font-size: 10.5px; }
</style>
</head>
<body>

<section class="card card-front" aria-label="Business card front">
  <div class="brand"><span class="brand-mark"></span>Velmar Global Components Ltd</div>
</section>

<section class="card card-back" aria-label="Business card back">
  <svg class="shapes" width="520" height="300" viewBox="0 0 520 300">
    <defs>
      <linearGradient id="panelBlue" x1="0" y1="0" x2="1" y2="1">
        <stop offset="0" stop-color="#0a62b0"/>
        <stop offset="1" stop-color="#0255a3"/>
      </linearGradient>
    </defs>
    <polygon points="0,0 255,0 370,300 0,300" fill="url(#panelBlue)"/>
    <rect x="503" y="0" width="17" height="300" fill="#0255a3"/>
    <rect x="268" y="108" width="44" height="44" fill="#9bcb3c"/>
    <rect x="285" y="152" width="44" height="44" fill="#3176b5"/>
    <rect x="302" y="196" width="44" height="44" fill="#0692cd"/>
    <path d="M290 119 a9 9 0 0 1 9 9 c0 7 -9 15 -9 15 s-9 -8 -9 -15 a9 9 0 0 1 9 -9z" fill="#fff"/>
    <circle cx="290" cy="128" r="3.2" fill="#9bcb3c"/>
    <path d="M298 165 l5 -2 l3 7 l-3 2 c1 4 4 7 8 8 l2 -3 l7 3 l-2 5 c-11 1 -21 -9 -20 -20z" fill="#fff"/>
    <rect x="313" y="207" width="22" height="22" fill="none" stroke="#fff" stroke-width="2"/>
    <rect x="317" y="212" width="14" height="2" fill="#fff"/>
    <rect x="317" y="217" width="14" height="2" fill="#fff"/>
    <rect x="317" y="222" width="14" height="2" fill="#fff"/>
  </svg>

  <div class="brand"><span class="brand-mark"></span><span>Velmar Global<br>Components Ltd</span></div>

  <div class="contact">
    <h1 class="contact-name">Dorian Pell</h1>
    <p class="contact-role">CEO/FOUNDER</p>
    <p class="contact-group">17 Tamsey Yard, Upper Drisk,<br>Warwick, CV31 8RJ, UK</p>
    <p class="contact-group">014-552-7301<br>014-552-7301</p>
    <p class="contact-group small">dorianpell@velmarparts-example.co.uk<br>www.velmarparts-example.co.uk</p>
  </div>
</section>

</body>
</html>
```